依頼詳細
現在使っているものを画像データで添付します。
事務所ロゴをフォトショップデータで添付します。

参考に、市販の表紙デザインにはこういったものがあります。(下記リンク)
https://www.kazane-dk.co.jp/store/products/list.php?category_id=23
https://tomoriworks.com/item/certificate/
http://mizuho-kanade.com/front_cover/
A4の紙を綴じるものなので、A3より一回り大きいA3ワイドのレザック紙に印刷しております。こちら302×430mmサイズです。

表紙には、お客様(権利者)の名前と
その下には不動産の表示が入ります。(案件ごとに印刷します)
そのため、こちらを手差し印刷できるよう、高さ5センチ程度の空白を空けておいていただきたいです。

サイズ:A3ワイド(302×430mm)
2つ折り、左開きです。半分に折った部分が表紙となります。

色、デザインの雰囲気等お任せいたします。
公的で固い重要書類をいれるものですが、そういったイメージにはあまり縛られずなるべくオリジナリティのあるものを使いたいと思います。
記載項目
不動産登記権利情報

司法書士ふじさわ事務所
希望イメージ
シンプル 複雑
単色 カラフル
暗い 明るい
日常 高級
遊び心 厳粛
未来的 伝統的
女性的 男性的
希望する色
設定なし
納品ファイル
• イラストレーター形式 (.ai)
補足説明
設定なし
【追記】桐のマークについて
現在使っている権利証表紙には、司法書士バッヂの意匠である五三桐花をいれておりますが、今回は特に使用の指定はしません。
桐のマークを入れる場合については、五三桐でお願いいたします(葉っぱが中央に5枚・左右に3枚ずつの家紋)

(参考)
http://senra-mokudo.com/kamon-c/cate0/kiri/kiri2.html
https://www.ezukan-store.jp/img344/225970_3130817.html
■ 選んだ理由

見た瞬間に目を惹くデザインだと思い、選ばせていただきました。

■ 提案者全員のお礼・コメント

たくさんのご提案をいただき大変嬉しく思っております。
皆様それぞれ、素敵なデザインを考えていただき本当にありがとうございます。

```html
<!DOCTYPE html>
<html lang="ja">
<head>
<meta charset="utf-8">
<title>不動産登記権利情報 表紙</title>
<link rel="stylesheet" href="https://fonts.googleapis.com/css2?family=Noto+Serif+JP:wght@500&family=Noto+Sans+JP:wght@400;700&display=swap">
<style>
  :root {
    --paper: #dfe6eb;
    --paper-deep: #cdd8e0;
    --pattern: #b9c9d5;
    --accent: #5f7f99;
    --rule: #7f98ad;
    --ink: #1f2c47;
  }
  html, body { margin: 0; padding: 0; overflow: hidden; }
  body { width: 854px; height: 1200px; background: #fff; }
  .cover {
    position: relative; width: 854px; height: 1200px; overflow: hidden;
    background: linear-gradient(160deg, var(--paper) 0%, #e6ecf0 50%, var(--paper-deep) 100%);
  }
  .cover__pattern { position: absolute; inset: 0; }
  .cover__crest {
    position: absolute; left: 598px; top: 72px; width: 118px; height: 112px;
    border-radius: 50% 50% 40% 40%;
    background: radial-gradient(circle, #f1f4f6 0%, #e4eaee 70%, rgba(228,234,238,0) 100%);
  }
  .cover__title {
    position: absolute; left: 214px; top: 336px; width: 450px; height: 62px;
    box-sizing: border-box; border: 2px solid var(--accent);
    display: flex; align-items: center; justify-content: center;
    font-family: "Noto Serif JP", serif; font-weight: 500; font-size: 38px;
    color: var(--accent); letter-spacing: 2px;
  }
  .cover__fill-line {
    position: absolute; left: 157px; width: 541px; height: 0;
    border-top: 2px solid var(--rule);
  }
  .cover__fill-line--name { top: 535px; }
  .cover__fill-line--property { top: 632px; }
  .office {
    position: absolute; left: 88px; top: 862px; display: flex; align-items: flex-start; gap: 16px;
    font-family: "Noto Sans JP", sans-serif; color: var(--ink);
  }
  .office__mark { width: 70px; height: 112px; border: 2px solid var(--ink); box-sizing: border-box; }
  .office__role { font-size: 15px; margin: 4px 0 0; letter-spacing: 1px; }
  .office__name { font-size: 50px; font-weight: 700; margin: 0; line-height: 1.15; letter-spacing: 3px; }
  .office__address, .office__tel { font-size: 11px; margin: 2px 0 0; letter-spacing: .5px; }
</style>
</head>
<body>
<main class="cover">
  <svg class="cover__pattern" width="854" height="1200" viewBox="0 0 854 1200">
    <polygon role="img" aria-label="麻の葉文様の装飾(左上)" points="0,0 190,0 0,230" fill="var(--pattern)" opacity=".35"/>
    <polygon role="img" aria-label="麻の葉文様の装飾(右上)" points="560,0 854,0 854,300 720,210" fill="var(--pattern)" opacity=".5"/>
    <polygon role="img" aria-label="麻の葉文様の装飾(右下)" points="854,700 854,1200 420,1200" fill="var(--pattern)" opacity=".55"/>
    <line x1="676" y1="40" x2="676" y2="860" stroke="var(--rule)" stroke-width="2"/>
    <line x1="692" y1="40" x2="692" y2="830" stroke="var(--rule)" stroke-width="2"/>
  </svg>
  <div class="cover__crest" role="img" aria-label="五三桐の紋"></div>

  <h1 class="cover__title">不動産登記権利情報</h1>
  <div class="cover__fill-line cover__fill-line--name"></div>
  <div class="cover__fill-line cover__fill-line--property"></div>

  <footer class="office">
    <div class="office__mark"></div>
    <div class="office__text">
      <p class="office__role">司法書士・行政書士</p>
      <p class="office__name">ふじさわ事務所</p>
      <p class="office__address">〒060-0000 北海道札幌市中央区若葉町3丁目2番5号</p>
      <p class="office__tel">TEL 011-555-0142　FAX 011-555-0143</p>
    </div>
  </footer>
</main>
</body>
</html>
```